Letter Head

We need a letter head desgn (A4).
Header Marcus Pellow Creative
phone number 0438705164
email marcuspellowcreative@fernmail.example

Footer ABN 37 512 640 915

```html
<!DOCTYPE html>
<html lang="en">
<head>
<meta charset="utf-8">
<title>Marcus Pellow Creative — Letterhead</title>
<link href="https://fonts.googleapis.com/css2?family=Arimo:wght@400;700&display=swap" rel="stylesheet">
<style>
  :root {
    --brand-green: #64c172;
    --tagline-green: #3fb36b;
    --brand-grey: #9b9b9b;
    --ink: #1e1e1e;
    --paper: #ffffff;
  }
  html, body {
    margin: 0;
    padding: 0;
    overflow: hidden;
    background: var(--paper);
  }
  .letterhead {
    position: relative;
    width: 848px;
    height: 1200px;
    overflow: hidden;
    background: var(--paper);
    font-family: "Arimo", Arial, sans-serif;
  }
  .corner-frames {
    position: absolute;
    inset: 0;
  }
  .corner-frames path {
    fill: var(--brand-green);
  }
  .vertical {
    position: absolute;
    transform: rotate(-90deg);
    transform-origin: top left;
    white-space: nowrap;
  }
  .brand {
    left: 59px;
    top: 357px;
    line-height: 1;
  }
  .brand-name {
    display: block;
    font-size: 18px;
    font-weight: 700;
    color: var(--brand-grey);
    letter-spacing: 0.1px;
  }
  .brand-tagline {
    display: block;
    margin-top: 2px;
    font-size: 12.5px;
    font-weight: 400;
    color: var(--tagline-green);
  }
  .brand-mark {
    position: absolute;
    left: 52px;
    top: 370px;
    width: 46px;
    height: 46px;
    background: var(--brand-grey);
  }
  .contact {
    left: 668px;
    top: 1114px;
    color: var(--ink);
  }
  .contact-phone {
    display: block;
    font-size: 17px;
    line-height: 21px;
    letter-spacing: 0.3px;
  }
  .contact-line {
    display: block;
    font-size: 12px;
    line-height: 14px;
  }
</style>
</head>
<body>
  <main class="letterhead">
    <svg class="corner-frames" width="848" height="1200" viewBox="0 0 848 1200" aria-hidden="true">
      <path class="frame-top" d="M55,52 Q55,40 67,40 H192 V63 H86 Q78,63 78,71 V127 H55 Z"/>
      <path class="frame-bottom" d="M795,1060 V1135 Q795,1147 783,1147 H658 V1125 H765 Q773,1125 773,1117 V1060 Z"/>
    </svg>

    <header class="brand vertical">
      <span class="brand-name">Marcus Pellow Creative</span>
      <span class="brand-tagline">Photography Video Design</span>
    </header>
    <div class="brand-mark" aria-hidden="true"></div>

    <footer class="contact vertical">
      <span class="contact-phone">0438. 705. 164</span>
      <span class="contact-line">www.mpcreative.example</span>
      <span class="contact-line">marcuspellowcreative@fernmail.example</span>
      <span class="contact-line">ABN 37 512 640 915</span>
    </footer>
  </main>
</body>
</html>
```